inspirational business card

I want to use the Vector on Pixavend.com (number 58172046) and I will purchase the vector to send it to the designer once the general concept is approved. You can download it for free for a one time use on providing a design for this request.
Within the vector, insert:
Tessa Brundle
Guidance and Partnering

I prefer a vertical card but do not require vertical.

Contact info:

Tessa Brundle, J.D.
Collaborative Lawyer
Certified Divorce Coach
Mediation Coach
PHONE 515/555-0143
EMAIL: tbjd@quellmail.net

Website: Guidanceandpartnering.com
Settlementcourse.com

I like greens, blue and grey. I do not want black font, and would like the font to be legible without needing perfect reading vision (no super small font).
I would like the overall theme to convey growth and nurturance.
I like the vector I selected because of the growth and light portrayed.
Not too frilly or too bold. I would like to to appeal to both sexes.

Target Market(s)

Generally professional women 35-60

Industry/Entity Type

Attorney

Font styles to use
Serif
Sans Serif

Colors
acd136
cadf82
fbf289
9d9d9d

Requirements
Must have
• My project does not need to have my photo but you could use it if you want
Nice to have
• Vertical
• I like rounded edges on the cards
Should not have
• I do not like my name appearing two times in close proximity. I'm not a flowery person.

```html
<!DOCTYPE html>
<html lang="en">
<head>
<meta charset="utf-8">
<title>Tessa Brundle – Business Card</title>
<link rel="stylesheet" href="https://fonts.googleapis.com/css2?family=Raleway:wght@400&family=Source+Sans+3:wght@400;600&display=swap">
<style>
  :root {
    --stage: #000000;
    --card-light: #f3f3f3;
    --card-dark: #212121;
    --ink: #4a524e;
    --rule: #6d7571;
    --brand-green: #7fb23d;
    --brand-grey: #9d9d9d;
    --mark-fill: #79a940;
    --web-text: #ffffff;
  }
  * { margin: 0; padding: 0; box-sizing: border-box; }
  html, body {
    width: 1200px;
    height: 900px;
    overflow: hidden;
    background: var(--stage);
  }
  .canvas {
    position: relative;
    width: 1200px;
    height: 900px;
    background: var(--stage);
    font-family: "Source Sans 3", "Helvetica Neue", Arial, sans-serif;
  }
  .card {
    position: absolute;
    top: 200px;
    width: 310px;
    height: 502px;
    text-align: center;
  }
  .card-front {
    left: 265px;
    background: var(--card-light);
    border-radius: 70px 0 70px 0;
    color: var(--ink);
  }
  .card-back {
    left: 641px;
    width: 309px;
    background: var(--card-dark);
    border-radius: 0 70px 0 70px;
  }
  .holder-name {
    position: absolute;
    top: 162px;
    left: 0; right: 0;
    font-size: 19px;
    line-height: 24px;
    font-weight: 600;
  }
  .holder-roles {
    position: absolute;
    top: 193px;
    left: 0; right: 0;
    font-size: 14px;
    line-height: 21px;
  }
  .divider {
    position: absolute;
    top: 273px;
    left: 74px;
    width: 162px;
    height: 2px;
    background: var(--rule);
  }
  .contact {
    position: absolute;
    top: 295px;
    left: 0; right: 0;
    font-size: 14px;
    line-height: 21px;
  }
  .brand-mark {
    position: absolute;
    top: 156px;
    left: 91px;
    width: 130px;
    height: 130px;
  }
  .brand-name {
    position: absolute;
    top: 292px;
    left: 0; right: 0;
    font-family: "Raleway", "Helvetica Neue", Arial, sans-serif;
    font-weight: 400;
  }
  .brand-name .name-line { display: block; font-size: 29px; line-height: 34px; color: var(--brand-green); }
  .brand-name .tag-line { display: block; font-size: 15px; line-height: 20px; color: var(--brand-grey); }
  .websites {
    position: absolute;
    top: 350px;
    left: 0; right: 0;
    font-size: 14px;
    line-height: 21px;
    color: var(--web-text);
  }
</style>
</head>
<body>
<main class="canvas">
  <section class="card card-front">
    <h1 class="holder-name">Tessa Brundle, J.D.</h1>
    <p class="holder-roles">Collaborative Lawyer<br>Certified Divorce Coach<br>Mediation Coach</p>
    <div class="divider"></div>
    <p class="contact">515/555-0143<br>tbjd@quellmail.net</p>
  </section>

  <section class="card card-back">
    <svg class="brand-mark" viewBox="0 0 130 130" aria-hidden="true">
      <circle cx="65" cy="65" r="63" fill="var(--mark-fill)"/>
    </svg>
    <p class="brand-name">
      <span class="name-line">Tessa Brundle</span>
      <span class="tag-line">Guidance and Partnering</span>
    </p>
    <p class="websites">www.Guidanceandpartnering.com<br>www.Settlementcourse.com</p>
  </section>
</main>
</body>
</html>
```